Plumbing Business Card Design

our business is a plumbing business.
we would like to see designs with our LOGO featured and then either purple or black writing with a white back ground
or black back ground with white or purple writing or even a purple card!
one option we would love to see is if you could get the TKR letters away from the white background ( it is currently in a white box as a jpeg )it is currently on and overlay it onto black.
FRONT
TKR image to be displayed on the front, please use the attached picture. ( you can remove the email address and mobile number from the botttom and re write it in different font or in a different place on the front.
Directly under the large TKR we would like the words Tidewell Kern Plumbing.
could be spread out like this T I D E W E L L K E R N
P L U M B I N G
We really are open to suggestions though!
Also on the front of the card we could like our little catch phrase somewhere Brindle's Local Plumber

we dont want in plumbing pictures or photos but we are open to swirl across the card or water movement or droplets.

BACK
These services need to be dot pointed or listed on the back
Hot & Cold Water Services
Gas Fitting
Bathroom & Kitchen Renovations
Metal Roofing & Guttering
New Homes & Extensions
Hot Water Service Changeovers
Drainage & Stormwater Works
All General Plumbing & Maitenance

in smaller writing or down the bottom of the card on the back please display write this Lic. No 473918

Contact Information for Business Card

Colm Kern
Mobile: 0427 391 206
email: tidewellkernplumbing@mailnest.example
FInd Us on Socialbook Tidewell Kern Plumbing ( with the f symbol ) either on the front or the back

```html
<!DOCTYPE html>
<html lang="en">
<head>
<meta charset="UTF-8">
<title>Tidewell Kern Plumbing — Business Cards</title>
<link href="https://fonts.googleapis.com/css2?family=Open+Sans:wght@400;600;700;800&display=swap" rel="stylesheet">
<style>
  :root {
    --bg: #e9e9ec;
    --card: #ffffff;
    --brand-blue: #3b78c8;
    --brand-purple: #6a4bb0;
    --ink: #151515;
    --ink-soft: #2a2a2a;
  }
  * { box-sizing: border-box; margin: 0; padding: 0; }
  html, body {
    width: 1200px; height: 900px; overflow: hidden;
    background: var(--bg);
    font-family: "Open Sans", Arial, sans-serif;
    color: var(--ink);
  }
  .canvas { position: relative; width: 1200px; height: 900px; }

  .card {
    position: absolute;
    width: 620px; height: 372px;
    background: var(--card);
    border-radius: 24px;
    overflow: hidden;
    box-shadow: 0 10px 28px rgba(0,0,0,0.18);
  }
  .card--back { left: 60px; top: 60px; }
  .card--front { left: 520px; top: 470px; }

  /* Wordmark */
  .wordmark {
    font-weight: 800;
    color: var(--brand-blue);
    letter-spacing: 4px;
    line-height: 1;
  }

  /* Back card */
  .card--back .wordmark {
    position: absolute; left: 40px; top: 38px;
    font-size: 96px;
  }
  .services {
    position: absolute; left: 40px; top: 168px;
  }
  .services__title {
    font-size: 17px; font-weight: 600;
    color: var(--brand-blue);
    letter-spacing: 0.5px;
    margin-bottom: 2px;
  }
  .services__list { list-style: none; }
  .services__list li {
    position: relative;
    padding-left: 24px;
    font-size: 17px; line-height: 21.5px;
    color: var(--ink-soft);
  }
  .services__list li::before {
    content: "";
    position: absolute; left: 2px; top: 6px;
    width: 11px; height: 11px; border-radius: 50%;
    background: var(--brand-blue);
  }
  .back-details {
    position: absolute; right: 34px; top: 176px;
    text-align: right;
    font-size: 16px; line-height: 23px;
    color: var(--ink-soft);
  }
  .back-details .social-dot {
    display: inline-block; width: 9px; height: 9px;
    border-radius: 50%; background: var(--brand-blue);
    margin-left: 6px; vertical-align: 2px;
  }

  /* Front card */
  .brand-lockup {
    position: absolute; right: 50px; top: 30px;
    text-align: center;
  }
  .card--front .wordmark { font-size: 92px; }
  .brand-lockup__name {
    margin-top: 8px;
    font-size: 22px; font-weight: 700;
    color: var(--brand-blue);
    letter-spacing: 6px;
    line-height: 28px;
  }
  .divider {
    position: absolute; left: 40px; right: 0; top: 262px;
    height: 2px; background: var(--brand-blue);
  }
  .contact {
    position: absolute; left: 44px; top: 222px;
  }
  .contact__name {
    font-size: 28px; font-weight: 700;
    letter-spacing: 0.5px; line-height: 34px;
    color: var(--ink);
  }
  .contact__row {
    display: flex; align-items: center; gap: 10px;
    font-size: 18px; font-weight: 600; line-height: 27px;
    color: var(--ink);
  }
  .contact__row:first-of-type { margin-top: 10px; }
  .contact__row svg { width: 14px; height: 14px; flex: none; }
  .corner-tab {
    position: absolute; left: 0; bottom: 0;
    width: 14px; height: 90px;
    background: var(--brand-blue);
  }
</style>
</head>
<body>
<main class="canvas">

  <section class="card card--back" aria-label="Card back">
    <div class="wordmark">TKR</div>
    <div class="services">
      <p class="services__title">SERVICES:</p>
      <ul class="services__list">
        <li>Hot &amp; Cold Water Services</li>
        <li>Gas Fitting</li>
        <li>Bathroom &amp; Kitchen Renovations</li>
        <li>Metal Roofing &amp; Guttering</li>
        <li>New Homes &amp; Extensions</li>
        <li>Hot Water Service Changeovers</li>
        <li>Drainage &amp; Stormwater Works</li>
        <li>All General Plumbing &amp; Maitenance</li>
      </ul>
    </div>
    <div class="back-details">
      <p>FInd Us on Socialbook:</p>
      <p>Tidewell Kern Plumbing<span class="social-dot"></span></p>
      <p>Lic. No 473918</p>
    </div>
  </section>

  <section class="card card--front" aria-label="Card front">
    <div class="brand-lockup">
      <div class="wordmark">TKR</div>
      <p class="brand-lockup__name">TIDEWELL KERN<br>PLUMBING</p>
    </div>
    <div class="divider"></div>
    <div class="contact">
      <p class="contact__name">COLM KERN</p>
      <p class="contact__row">
        <svg viewBox="0 0 24 24" aria-hidden="true"><path fill="#3b78c8" d="M6.6 10.8a15.1 15.1 0 0 0 6.6 6.6l2.2-2.2a1 1 0 0 1 1-.25 11.4 11.4 0 0 0 3.6.57 1 1 0 0 1 1 1V20a1 1 0 0 1-1 1A17 17 0 0 1 3 4a1 1 0 0 1 1-1h3.5a1 1 0 0 1 1 1c0 1.25.2 2.45.57 3.57a1 1 0 0 1-.25 1z"/></svg>
        0427 391 206
      </p>
      <p class="contact__row">
        <svg viewBox="0 0 24 24" aria-hidden="true"><rect x="2.5" y="5" width="19" height="14" rx="2" fill="none" stroke="#3b78c8" stroke-width="2"/><path d="M3 6l9 7 9-7" fill="none" stroke="#3b78c8" stroke-width="2"/></svg>
        tidewellkernplumbing@mailnest.example
      </p>
    </div>
    <div class="corner-tab"></div>
  </section>

</main>
</body>
</html>
```